Web Design Project - Valdora Homes

We would like you to refine our web layouts for a (1) homepage and (2) a product page (see attached files for reference).

The client is a swiss construction company, that designs, builds and sells standardized and tailored-made residential houses.

His logo is old, but not up for redesign. The only way to salvage it, is to incorporate its yellow color (as highlight) to the overall design, so as to create some brand awareness.

REQUIREMENTS FOR THE HOMEPAGE:
1. telephone number over menu
2. logo + menu with 6 categories
3. slider for showing various house types (for pics, see attachments)
4. "AKTUELL" card with yellow color (to show his most actual projects) and a strong Call For Action (what in German would be: KONTAKT AUFNEHMEN)
5. a yellow stripe for his company's slogan (Ihr Partner für individuelle und normierte Wohnbauten)
6. A left coloumn with
(a) two picture-holders under the title REFERENZEN
(b) the three supporting logos of TERVIK, SOLVARIN and VB KLIMABAU VERBUND (can be downloaded as pngs)
7. A right column with 6 headlines + texts of 3 lines each
8. a footer with the adress info

REQUIREMENTS FOR PRODUKT PAGE:
1. slider for pictures
2. info box with Call For Action for particular House-types
3. thumbnail pics under the slider for additional images of any particular house type
4. Left-side: name of house type and picture
5. Right-side: Header and blindtext for house description
6. three placeholders for 3 floor plans
Updates

NB No coding necessary. An imaginative, fresh design along the layout requirements will do.
Thanx to all

To all those who had probs with the downloading of the attached files:
we've posted a new Zip.
Have a look!
thankx

Thanks to everyone who participated.
We will be showing a selection of your designs to the client within the next couple of days.
We'll get back to you, as soon as possible.

Industry/Entity Type

Construction

Requirements
Must have
• - slider
- info box with call for action
- thumbnail pictures
- fresh look based on colors, design of elements (slider, info box), font selection

```html
<!DOCTYPE html>
<html lang="de">
<head>
<meta charset="utf-8">
<title>Valdora Homes</title>
<link href="https://fonts.googleapis.com/css2?family=Questrial&family=Roboto:wght@400;500&display=swap" rel="stylesheet">
<style>
:root{
  --bg:#f2f2f2;
  --blue:#0f2f85;
  --blue-deep:#0a2470;
  --yellow:#f2c300;
  --yellow-dark:#d19a00;
  --navy-text:#1a3a8e;
  --grey-text:#666;
  --nav-text:#5e5e5e;
  --black:#000;
  --line:#dcdcdc;
}
*{box-sizing:border-box;margin:0;padding:0}
html,body{width:1038px;height:1200px;overflow:hidden;background:var(--bg)}
body{position:relative;font-family:"Roboto",Arial,sans-serif;color:var(--grey-text)}
.abs{position:absolute}
.topbar{left:0;top:0;width:1038px;height:8px;background:var(--black)}
.phone-tab{left:782px;top:8px;width:150px;height:23px;background:var(--black);color:#fff;font:500 11px "Roboto",sans-serif;letter-spacing:.2px;display:flex;align-items:center;justify-content:center}
.brand{left:108px;top:34px;display:flex;align-items:center;gap:6px;font:400 17px "Questrial",sans-serif;color:#222}
.brand-mark{width:12px;height:12px;background:var(--yellow)}
.nav{right:104px;top:44px;display:flex;gap:20px;font:500 12.5px "Roboto",sans-serif;color:var(--nav-text);letter-spacing:.1px}
.hero-band{left:0;top:98px;width:1038px;height:420px;background:var(--blue)}
.hero-photo{left:104px;top:125px;width:830px;height:364px;background:linear-gradient(180deg,#b9d3ee 0%,#cfdfee 28%,#a6a39c 45%,#8d8a84 75%,#b4aea4 100%);box-shadow:0 12px 14px -8px rgba(0,0,0,.45)}
.dots{left:466px;top:465px;width:114px;height:24px;background:#e9e9e9;border-radius:7px 7px 0 0;display:flex;align-items:center;justify-content:center;gap:6px}
.dots span{width:10px;height:10px;border-radius:50%;background:#8a8a8a}
.dots span.on{background:#c98c3a}
.news{left:104px;top:535px;width:544px;height:62px;background:var(--yellow-dark)}
.news-label{left:0;top:0;width:100px;height:62px;background:var(--yellow);color:#fff;font:400 12.5px "Questrial",sans-serif;display:flex;align-items:center;padding-left:15px}
.news-arrow{left:100px;top:0}
.news-thumb{left:111px;top:5px;width:70px;height:52px;border:2px solid #fff;background:linear-gradient(180deg,#b7cfe6 0%,#c8c1b2 55%,#7e9a5c 100%)}
.news-title{left:190px;top:9px;font:500 10px "Roboto",sans-serif;color:#fff}
.news-text{left:190px;top:26px;width:350px;font:400 10px/15.5px "Roboto",sans-serif;color:#fff}
.cta{left:672px;top:535px;width:262px;height:63px;background:linear-gradient(180deg,#1f47b4 0%,var(--blue-deep) 100%);display:flex;align-items:center;padding-left:15px;gap:12px;color:#fff;font:400 16px "Questrial",sans-serif;letter-spacing:.2px}
.cta-icon{width:32px;height:32px;border-radius:50%;background:#fff;display:flex;align-items:center;justify-content:center}
.section-head{left:104px;top:621px;width:545px;height:45px;background:#fbfbfb;border:1px solid #e2e2e2;color:var(--yellow);font:400 19px "Questrial",sans-serif;display:flex;align-items:center;padding-left:7px}
.ref{top:679px;width:260px}
.ref-photo{width:260px;height:136px}
.ref-title{margin-top:12px;color:var(--yellow);font:400 16px "Questrial",sans-serif;margin-left:-2px}
.ref-text{margin-top:6px;font:400 10px/15.6px "Roboto",sans-serif;text-align:justify;color:#707070;margin-left:-2px}
.btn{display:inline-block;margin-top:11px;background:var(--black);color:#fff;font:400 12.5px "Questrial",sans-serif;padding:8px 8px 7px}
.partners{left:104px;top:984px;width:545px;height:73px;border-top:1px solid var(--line);border-bottom:1px solid var(--line);display:flex;align-items:center;justify-content:space-between;padding:0 6px}
.partner{display:flex;align-items:center;gap:6px;font:400 14px "Questrial",sans-serif;color:#444}
.partner i{width:12px;height:12px;display:block}
.news-list{left:672px;top:622px;width:262px}
.news-item{height:72.5px;border:1px solid #e2e2e2;background:#fbfbfb;padding:8px 7px}
.news-item h3{font:400 12px "Questrial",sans-serif;color:var(--navy-text);margin-bottom:8px}
.news-item p{font:400 9.8px/15px "Roboto",sans-serif;color:#707070;text-align:justify}
.footer{left:0;top:1082px;width:1038px;height:118px;background:var(--black)}
.address{left:106px;top:14px;font:400 10px/15.6px "Roboto",sans-serif;color:#9a9a9a}
.address .gap{margin-top:3px}
.address a{color:var(--yellow);text-decoration:none}
.social{left:757px;top:37px;display:flex;gap:5px}
.social span{width:26px;height:26px;border-radius:50%;background:#3a3a3a}
.copy{left:790px;top:89px;font:400 10px "Roboto",sans-serif;color:#8a8a8a}
</style>
</head>
<body>
<div class="abs topbar"></div>
<div class="abs phone-tab">TELEFON&nbsp; 071 555 20 40</div>
<div class="abs brand"><span class="brand-mark"></span>Valdora Homes</div>
<nav class="abs nav">
  <span>REFERENCES</span><span>HOUSE TYPES</span><span>SPECIAL OFFER</span><span>NEW BUILDINGS</span><span>SERVICES</span><span>COMPANY</span>
</nav>

<div class="abs hero-band"></div>
<div class="abs hero-photo" role="img" aria-label="Slider photo: two-storey house with grey siding, white trim and front porch under a blue sky"></div>
<div class="abs dots"><span></span><span></span><span class="on"></span><span></span><span></span><span></span></div>

<div class="abs news">
  <div class="abs news-label">AKTUELL</div>
  <svg class="abs news-arrow" width="24" height="62"><polygon points="0,0 24,31 0,62" fill="var(--yellow)"/></svg>
  <div class="abs news-thumb" role="img" aria-label="Thumbnail photo of a single-storey house"></div>
  <div class="abs news-title">SED DO EIUSMOD TEMPOR</div>
  <div class="abs news-text">sed do eiusmod tempor incididunt ut labore et dolore magna aliqua.Ut enim minim veniam, quis nostrud exercitation ullamco laboris nisi ut aliquip ex ea</div>
</div>

<div class="abs cta">
  <span class="cta-icon"><svg width="18" height="16" viewBox="0 0 18 16"><path d="M1 5c0-3 16-3 16 0v2h-4V5H5v2H1z" fill="#222"/><rect x="3" y="8" width="12" height="7" rx="1.5" fill="#222"/><circle cx="9" cy="11.5" r="2" fill="#fff"/></svg></span>
  KONTAKT AUFNEHMEN
</div>

<div class="abs section-head">REFERENZEN</div>

<div class="abs ref" style="left:104px">
  <div class="ref-photo" role="img" aria-label="Reference photo: brick two-storey house with garage" style="background:linear-gradient(180deg,#9fc2e4 0%,#b9cde0 30%,#8a7466 55%,#d9d6cf 80%,#a5a08f 100%)"></div>
  <div class="ref-title">SED DO EIUSMOD TEMPOR</div>
  <div class="ref-text">sed do eiusmod tempor incididunt ut labore et dolore magna aliqua.Ut enim adminim veniam, quis nostrud exenim adminim veniam, quis nostrud exerveniam, quis nostrud exenim adminim veniam, quis nostrud exer</div>
  <span class="btn">DETAILS</span>
</div>
<div class="abs ref" style="left:389px">
  <div class="ref-photo" role="img" aria-label="Reference photo: beige two-storey house with porch" style="background:linear-gradient(180deg,#f3eef2 0%,#e6ddc4 35%,#d8caa4 65%,#b49c80 100%)"></div>
  <div class="ref-title">SED DO EIUSMOD TEMPOR</div>
  <div class="ref-text">sed do eiusmod tempor incididunt ut labore et dolore magna aliqua.Ut enim adminim veniam, quis nostrud exenim adminim veniam, quis nostrud exerveniam, quis nostrud exenim adminim veniam, quis nostrud exer</div>
  <span class="btn">DETAILS</span>
</div>

<div class="abs partners">
  <div class="partner"><i style="background:#3d9a3a"></i>TERVIK</div>
  <div class="partner"><i style="background:#d0282e"></i>SOLVARIN</div>
  <div class="partner"><i style="background:#b3262b"></i>VB KLIMABAU VERBUND</div>
</div>

<div class="abs news-list">
  <div class="news-item"><h3>Sed do Eiusmod Tempor</h3><p>sed do eiusmod tempor incididunt ut labore et dolore magna aliqua.Ut enim adminim veniam, quis nostrud</p></div>
  <div class="news-item"><h3>labore do Eiusmod Tempor</h3><p>sed do eiusmod tempor incididunt ut labore et dolore magna aliqua.Ut enim adminim veniam, quis nostrud</p></div>
  <div class="news-item"><h3>Sed do Eiusmod Dolore</h3><p>sed do eiusmod tempor incididunt ut labore et dolore magna aliqua.Ut enim adminim veniam, quis nostrud</p></div>
  <div class="news-item"><h3>magna utEiusmod Tempor</h3><p>sed do eiusmod tempor incididunt ut labore et dolore magna aliqua.Ut enim adminim veniam, quis nostrud</p></div>
  <div class="news-item"><h3>Eiusmod usmod Tempor</h3><p>sed do eiusmod tempor incididunt ut labore et dolore magna aliqua.Ut enim adminim veniam, quis nostrud</p></div>
  <div class="news-item"><h3>tempor Eiusmod Tempor</h3><p>sed do eiusmod tempor incididunt ut labore et dolore magna aliqua.Ut enim adminim veniam, quis nostrud</p></div>
</div>

<footer class="abs footer">
  <div class="abs address">
    Valdora Homes GmbH<br>Fam. Berling<br>Lindenweg 14 CH-8400 Musterdorf
    <div class="gap">Telefon 071 555 20 40<br>Telefax 071 555 20 41<br><a>info@valdora-homes.ch</a></div>
  </div>
  <div class="abs social"><span></span><span></span><span></span><span></span><span></span><span></span></div>
  <div class="abs copy">© 2013&nbsp; valdora-homes.</div>
</footer>
</body>
</html>
```